business card design for luxurious real estate brand

using the attached logo, i am looking for a 2-sided business card design. the back should be the gold logo on black background. the front needs to include: gold logo, name, phone, email, and website

Industry/Entity Type

real estate

Contact Information for Business Card

logo, name, email, phone, website

Font styles to use
Sans Serif

```html
<!DOCTYPE html>
<html lang="en">
<head>
<meta charset="utf-8">
<title>Casa Meridian – Business Card</title>
<link href="https://fonts.googleapis.com/css2?family=Montserrat:wght@400;500;700&family=Open+Sans:wght@400&display=swap" rel="stylesheet">
<style>
  :root{
    --stage:#2a2a2d;
    --card:#1f1f22;
    --card-deep:#141416;
    --gold:#e6b422;
    --gold-light:#f7d44a;
    --gold-dark:#b8860b;
    --white:#f2f2f2;
  }
  *{box-sizing:border-box;margin:0;padding:0}
  html,body{width:1200px;height:780px;overflow:hidden}
  body{
    background:var(--stage);
    display:flex;align-items:center;justify-content:center;gap:40px;
    font-family:"Open Sans",sans-serif;
  }
  .card{
    position:relative;width:540px;height:309px;
    background:var(--card);
    border-left:5px solid var(--gold);
    border-bottom:5px solid var(--gold);
    overflow:hidden;
    box-shadow:0 18px 40px rgba(0,0,0,.55);
  }
  .card__pattern{
    position:absolute;inset:0;
    background:linear-gradient(135deg,#26262a 0%,#1c1c1f 50%,#29292d 100%);
  }
  .brand{
    position:absolute;display:flex;align-items:center;gap:12px;
    font-family:"Montserrat",sans-serif;font-weight:500;
    color:var(--gold);letter-spacing:.28em;text-transform:uppercase;
    white-space:nowrap;
  }
  .brand__square{width:14px;height:14px;background:var(--gold);flex:none}
  .card--back .brand{right:40px;top:136px;font-size:17px}
  .card--front .brand{left:34px;top:96px;font-size:26px;letter-spacing:.22em}
  .card--front .brand__square{width:24px;height:24px}

  .person{
    position:absolute;right:48px;top:30px;text-align:right;
    font-family:"Montserrat",sans-serif;
  }
  .person__name{font-weight:700;font-size:24px;color:var(--gold);line-height:1.1}
  .person__role{font-weight:400;font-size:13px;color:var(--white);margin-top:4px;letter-spacing:.02em}
  .person__bar{position:absolute;right:28px;top:30px;width:8px;height:44px;
    background:linear-gradient(180deg,var(--gold-light),var(--gold-dark))}

  .feature{
    position:absolute;right:0;bottom:0;width:195px;height:165px;
    background:linear-gradient(160deg,#2a2a2e 0%,#0d0d0f 70%);
  }
  .contacts{
    position:absolute;left:34px;bottom:28px;list-style:none;
    display:flex;flex-direction:column;gap:8px;
  }
  .contacts__item{display:flex;align-items:center;gap:10px;color:var(--white);font-size:14px}
  .contacts__icon{width:14px;height:14px;flex:none}
</style>
</head>
<body>

  <section class="card card--back" aria-label="Card back">
    <div class="card__pattern" role="img" aria-label="Tone-on-tone embossed pattern of the brand mark"></div>
    <div class="brand"><span class="brand__square"></span>Casa Meridian</div>
  </section>

  <section class="card card--front" aria-label="Card front">
    <div class="person">
      <p class="person__name">Livia Marchetti</p>
      <p class="person__role">Managing Director</p>
    </div>
    <span class="person__bar"></span>

    <div class="brand"><span class="brand__square"></span>Casa Meridian</div>

    <div class="feature" role="img" aria-label="Large black embossed brand mark"></div>

    <ul class="contacts">
      <li class="contacts__item">
        <svg class="contacts__icon" viewBox="0 0 24 24" fill="var(--gold)"><path d="M6.6 10.8a15.1 15.1 0 0 0 6.6 6.6l2.2-2.2a1 1 0 0 1 1-.25 11.4 11.4 0 0 0 3.6.57 1 1 0 0 1 1 1V20a1 1 0 0 1-1 1A17 17 0 0 1 3 4a1 1 0 0 1 1-1h3.5a1 1 0 0 1 1 1c0 1.250.2 2.450.57 3.57a1 1 0 0 1-.25 1z"/></svg>
        (555) 014-2738
      </li>
      <li class="contacts__item">
        <svg class="contacts__icon" viewBox="0 0 24 24" fill="var(--gold)"><path d="M3 5h18a1 1 0 0 1 1 1v12a1 1 0 0 1-1 1H3a1 1 0 0 1-1-1V6a1 1 0 0 1 1-1zm1 2.3V17h16V7.3l-8 5.2z M4.8 7 12 11.7 19.2 7z"/></svg>
        hello@casameridian.example
      </li>
      <li class="contacts__item">
        <svg class="contacts__icon" viewBox="0 0 24 24" fill="none" stroke="var(--gold)" stroke-width="2"><circle cx="12" cy="12" r="9"/><path d="M3 12h18M12 3c3 3.5 3 14.5 0 18M12 3c-3 3.5-3 14.5 0 18"/></svg>
        www.casameridian.example
      </li>
    </ul>
  </section>

</body>
</html>
```